Create a memorable Web Design for real estate branding

we are a Minnepolis brokerage and boutique housing specialist with over 27 years of experience in the Global furnished housing industry, servicing the Greater Los Angeles area. Specializing in “warm environments” we offer a customized approach to satisfying our guests and client’s needs by offering a wide array of options in highly desirable areas. Additionally, Lantern Dwelling Partners offers assistance and expertise to home buyers, sellers and investors.

Industry/Entity Type

Real Estate

Number of Pages Required

1 page

Font styles to use
Serif
Sans Serif
Decorative

```html
<!DOCTYPE html>
<html lang="en">
<head>
<meta charset="utf-8">
<title>Arlen Sorel Real Estate</title>
<link href="https://fonts.googleapis.com/css2?family=Didact+Gothic&display=swap" rel="stylesheet">
<style>
:root{
  --page:#053f38;
  --panel:#7bb344;
  --nav:#8cc23c;
  --nav-active:#a9d33a;
  --drop:#a6d235;
  --ink:#0b5a4c;
  --ink-dark:#0a4a3f;
  --faded:#5e9a45;
  --button:#12806a;
  --white:#ffffff;
}
*{margin:0;padding:0;box-sizing:border-box}
html,body{width:1008px;height:1200px;overflow:hidden}
body{background:var(--page);font-family:"Didact Gothic",sans-serif;color:var(--ink);position:relative}
.abs{position:absolute}
.brand{left:234px;top:10px;color:#2fb59a;font-size:20px;line-height:20px}
.brand small{display:block;font-size:10px;letter-spacing:1px;line-height:12px;margin-left:48px}
.social{left:678px;top:20px;display:flex;gap:7.5px}
.social span{width:10px;height:10px;background:#d8e6e0;border-radius:2px}
.nav{left:216px;top:51px;width:576px;height:33px;background:var(--nav);display:flex}
.nav a{height:33px;line-height:33px;text-align:center;font-size:9px;color:var(--ink);text-decoration:none;border-right:1px solid var(--ink-dark)}
.nav a.active{background:var(--nav-active)}
.dropdown{left:278px;top:90px;width:120px;height:77px;background:var(--drop);padding:8px 14px 0;font-size:7px;box-shadow:1px 2px 3px rgba(0,0,0,.25);z-index:2}
.dropdown div{height:24px;line-height:12px;border-bottom:1px solid var(--ink)}
.dropdown div:last-child{border:0}
.panel{left:216px;top:102px;width:576px;height:971px;background:var(--panel)}
.photo{background:linear-gradient(135deg,#3b3a36,#b9b2a5 45%,#a68058 75%,#6b5a45)}
.slider{left:234px;top:120px;width:540px;height:240px}
.circle-btn{width:14px;height:14px;border-radius:50%;background:var(--ink)}
.dot{width:7px;height:7px;border-radius:50%;background:var(--ink)}
.tagline{left:234px;top:398px;width:540px;text-align:center;font-style:italic;font-size:14px;line-height:19px;color:var(--ink)}
.rule{left:234px;width:540px;height:4px;border-top:1.5px solid var(--ink);border-bottom:1.5px solid var(--ink)}
.h2{font-size:11px;color:var(--ink);text-transform:uppercase}
.body-text{font-size:7.2px;line-height:12px;color:var(--ink)}
.list{left:606px;top:504px;width:170px}
.list li{list-style:none;position:relative;padding-left:11px}
.list li:before{content:"›";position:absolute;left:0}
.feature{width:117px;top:579px;text-align:center}
.feature .pic{height:62px}
.feature h3{font-weight:normal;font-size:10.5px;line-height:12px;margin-top:2px}
.feature p{font-size:7px;line-height:12px}
.thumb{top:742px;width:96px;height:77px}
.post{left:234px;width:115px;height:39px;border-bottom:1px dotted #5a8f3f}
.post b{position:absolute;left:0;top:0;font-weight:normal;font-size:15px;line-height:15px}
.post i{position:absolute;left:1px;top:15px;font-style:normal;font-size:6.5px}
.post p{position:absolute;left:28px;top:0;font-size:7px;line-height:12px}
.snap{width:33px;height:33px;background:#2e2e2e}
.chat{left:514px;width:120px;padding-left:8px;font-size:7px;line-height:12px;position:absolute;border-bottom:1px dotted #5a8f3f;height:48px}
.chat:before{content:"›";position:absolute;left:0}
.field{left:657px;width:117px;background:var(--white);border:1px solid #cfcfcf}
.submit{left:658px;top:1031px;width:54px;height:16px;background:var(--button);color:var(--white);font-size:8px;text-align:center;line-height:16px}
.footer{left:216px;top:1086px;width:576px;height:32px;background:var(--nav);text-align:center;font-size:7px;line-height:32px}
</style>
</head>
<body>
<div class="abs brand">Arlen Sorel<small>REAL ESTATE</small></div>
<div class="abs social" aria-hidden="true"><span></span><span></span><span></span><span></span><span></span><span></span><span></span></div>

<nav class="abs nav">
  <a class="active" style="width:61px">Home</a>
  <a style="width:71px">Gallery</a>
  <a style="width:67px">Promotion</a>
  <a style="width:66px">Service</a>
  <a style="width:54px">Blog</a>
  <a style="width:69px">Contact</a>
</nav>
<div class="abs dropdown"><div>House Gallery</div><div style="margin-top:0">Interior Gallery</div><div>etc</div></div>

<main class="abs panel"></main>
<div class="abs slider photo" role="img" aria-label="Modern open-plan kitchen with wooden steps and dark staircase"></div>
<div class="abs circle-btn" style="left:463px;top:368px"></div>
<div class="abs dot" style="left:484px;top:372px"></div>
<div class="abs dot" style="left:495px;top:372px"></div>
<div class="abs dot" style="left:506px;top:372px"></div>
<div class="abs dot" style="left:517px;top:372px"></div>
<div class="abs circle-btn" style="left:531px;top:368px"></div>
<p class="abs tagline">We are a Minnepolis brokerage and boutique housing specialist with over 27<br>years of experience in the Global furnished housing industry.</p>
<div class="abs rule" style="top:455px"></div>

<h2 class="abs h2" style="left:234px;top:482px">Why we were better?</h2>
<p class="abs body-text" style="left:234px;top:504px;width:356px">we are a Minnepolis brokerage and boutique housing specialist with over 27 years of experience in the Global furnished housing industry, servicing the Greater Los Angeles area. Specializing in “warm environments” we offer a customized approach to satisfying our guests and client’s needs by offering a wide array of options in highly desirable areas. Additionally, Lantern Dwelling Partners offers</p>
<ul class="abs body-text list" style="font-size:8px"><li>we are a Minnepolis brokerage and</li><li>boutique housing specialist with over 27</li><li>years of experience in the Global fur-</li><li>nished housing industry, servicing the</li></ul>

<div class="abs feature" style="left:234px"><div class="pic photo" style="background:linear-gradient(135deg,#f5f5f0,#a9ad8e 50%,#6e7a5a)" role="img" aria-label="Small house folded from banknotes"></div><h3>INVESTMENT</h3><p>we are a Minnepolis brokerage and boutique housing specialist with over 27 years of experience</p></div>
<div class="abs feature" style="left:374px"><div class="pic photo" style="background:linear-gradient(180deg,#d8dadc,#5f6670 55%,#7a5040)" role="img" aria-label="Hands holding a model house"></div><h3>INSURANCE</h3><p>we are a Minnepolis brokerage and boutique housing specialist with over 27 years of experience</p></div>
<div class="abs feature" style="left:516px"><div class="pic photo" style="background:linear-gradient(180deg,#3d7fd0,#c9a065 45%,#4f9a3a)" role="img" aria-label="Children running on a school lawn"></div><h3>CHILDREN CARE</h3><p>we are a Minnepolis brokerage and boutique housing specialist with over 27 years of experience</p></div>
<div class="abs feature" style="left:657px"><div class="pic photo" style="background:linear-gradient(180deg,#a9c4e0,#d6c0a0 60%,#9a7050)" role="img" aria-label="Builder carrying timber at a house frame"></div><h3>BETTER MATERIAL</h3><p>we are a Minnepolis brokerage and boutique housing specialist with over 27 years of experience</p></div>
<div class="abs" style="left:234px;top:693px;width:540px;border-top:1px solid var(--ink)"></div>

<h2 class="abs h2" style="left:234px;top:718px;color:var(--faded)">House Product</h2>
<div class="abs circle-btn" style="left:744px;top:717px;width:13px;height:13px"></div>
<div class="abs circle-btn" style="left:761px;top:717px;width:13px;height:13px"></div>
<div class="abs thumb photo" style="left:234px" role="img" aria-label="Interior with wooden steps"></div>
<div class="abs thumb photo" style="left:345px;background:linear-gradient(135deg,#b0643a,#efe6da 50%,#c9a985)" role="img" aria-label="Bright living room with wood ceiling"></div>
<div class="abs thumb photo" style="left:456px;background:linear-gradient(180deg,#7fa8e0,#f1f1f1 45%,#5f8a3a)" role="img" aria-label="White two-storey family house"></div>
<div class="abs thumb photo" style="left:567px;background:linear-gradient(180deg,#a3c8e8,#6b3a2a 45%,#2f6a45)" role="img" aria-label="Modern brick townhouse"></div>
<div class="abs thumb photo" style="left:678px;background:linear-gradient(180deg,#dfe7ee,#8a6a5a 45%,#e8e8e8)" role="img" aria-label="Three-storey modern villa"></div>
<div class="abs rule" style="top:842px"></div>

<h2 class="abs h2" style="left:234px;top:869px">Latest Posts</h2>
<h2 class="abs h2" style="left:374px;top:869px">Snapshots</h2>
<h2 class="abs h2" style="left:514px;top:869px">Chatter</h2>
<h2 class="abs h2" style="left:656px;top:869px">Contact Us</h2>

<div class="abs post" style="top:895px"><b>22</b><i>JUN</i><p>we are a Minnepolis<br>brokerage and boutique</p></div>
<div class="abs post" style="top:931px"><b>01</b><i>MAY</i><p>we are a Minnepolis<br>brokerage and boutique</p></div>
<div class="abs post" style="top:970px"><b>17</b><i>FEB</i><p>we are a Minnepolis<br>brokerage and boutique</p></div>
<div class="abs post" style="top:1009px;border:0"><b>25</b><i>JAN</i><p>we are a Minnepolis<br>brokerage and boutique</p></div>

<div class="abs snap" style="left:374px;top:896px"></div><div class="abs snap" style="left:417px;top:896px"></div><div class="abs snap" style="left:459px;top:896px"></div>
<div class="abs snap" style="left:374px;top:938px"></div><div class="abs snap" style="left:417px;top:938px"></div><div class="abs snap" style="left:459px;top:938px"></div>
<div class="abs snap" style="left:374px;top:980px"></div><div class="abs snap" style="left:417px;top:980px"></div><div class="abs snap" style="left:459px;top:980px"></div>

<div class="chat" style="top:894px">Vivamus soder pharetra libero atincidunt Curabitur at ante sed nunc euismod sodales.</div>
<div class="chat" style="top:944px">Vivamus soder pharetra libero atincidunt Curabitur at ante sed nunc euismod sodales.</div>
<div class="chat" style="top:995px;border:0">Vivamus soder pharetra libero atincidunt Curabitur at ante sed nunc euismod sodales.</div>

<div class="abs field" style="top:897px;height:20px"></div>
<div class="abs field" style="top:925px;height:20px"></div>
<div class="abs field" style="top:953px;height:70px"></div>
<div class="abs submit">Submit</div>

<footer class="abs footer">© 2016 Arlen Sorel. All Right Reserved.</footer>
</body>
</html>
```